Business Card Design for BrightlaneReach.com

--I need a business card design for my company BrightlaneReach.com

I have attached my logo...I want the brightlane reach logo on the front of the business card, and then I want The Brightlane Chief on the back of it with my information.

I would like to see a light colored background as well as a dark colored background

FRONT:
BRIGHTLANE REACH LOGO
247 E. Pelham Row
5th Floor
San Diego CA 92384
www.BrightlaneReach.com

Advanced Website & App Development
Websites, Apps, Online Voucher Systems

Leading Edge Marketing Services
SMS, VB, SMM, SEM,

BACK:
BRIGHTLANE CHIEF LOGO
Dorian Welker
The Brightlane Chief
Call Or Text: 555-204-3378
Dorian@BrightlaneChief.com
www.BrightlaneChief.com

Target Market(s)

small business owners

Industry/Entity Type

Business Consultant

Contact Information for Business Card

FRONT:
BRIGHTLANE REACH LOGO
247 E. Pelham Row
5th Floor
San Diego CA 92384
www.BrightlaneReach.com

SMS, VB, SMM, SEM,

BACK:
BRIGHTLANE CHIEF LOGO
Dorian Welker
The Brightlane Chief
Dorian@BrightlaneChief.com
www.BrightlaneChief.com

Requirements
Must have
• add this quote on it somewhere, anywhere,preferrably on back
• "The Fastest Way To Success Is To Take Action”
• — Dorian Welker, Brightlane Chief
Nice to have
• open
Should not have
• red

```html
<!DOCTYPE html>
<html lang="en">
<head>
<meta charset="utf-8">
<title>Brightlane Reach – Business Card</title>
<link rel="stylesheet" href="https://fonts.googleapis.com/css2?family=Oswald:wght@300;400&family=Tinos:wght@400;700&display=swap">
<style>
  :root {
    --backdrop: #d4d4d4;
    --card: #ffffff;
    --brand-blue: #1a7fb5;
    --band-blue: #1b6fa6;
    --ink: #3a3a3a;
    --muted: #7a7a7a;
    --quote-author: #5a5a5a;
    --underline: #8bb6d3;
  }
  * { margin: 0; padding: 0; box-sizing: border-box; }
  html, body { width: 1200px; height: 800px; overflow: hidden; }
  body { background: var(--backdrop); position: relative; font-family: "Tinos", serif; }

  .card {
    position: absolute;
    top: 283px;
    width: 430px;
    height: 239px;
    background: var(--card);
  }
  .card--chief { left: 110px; }
  .card--reach { left: 638px; }

  .card__bands { position: absolute; inset: 0; width: 430px; height: 239px; }
  .card__bands polygon { fill: var(--band-blue); }

  /* Chief side */
  .brand-name {
    position: absolute;
    margin: 0;
    color: var(--brand-blue);
    font-family: "Oswald", sans-serif;
    font-weight: 400;
    line-height: 1;
    white-space: nowrap;
  }
  .brand-name--chief {
    right: 234px;
    top: 112px;
    font-size: 20px;
    letter-spacing: 1.5px;
    text-align: right;
  }

  .quote {
    position: absolute;
    right: 234px;
    top: 161px;
    text-align: right;
    font-family: "Oswald", sans-serif;
    font-weight: 300;
    font-size: 9px;
    color: var(--muted);
    line-height: 16px;
    text-transform: uppercase;
    white-space: nowrap;
  }
  .quote__author { color: var(--quote-author); }

  .contact { position: absolute; left: 263px; top: 87px; color: var(--ink); }
  .contact__row { position: absolute; left: 0; display: flex; align-items: flex-start; white-space: nowrap; }
  .contact__icon { width: 10px; height: 10px; margin-top: 2px; margin-right: 7px; fill: var(--brand-blue); flex: none; }
  .contact__name {
    font-weight: 700;
    font-size: 14px;
    line-height: 14px;
    text-decoration: underline;
    text-decoration-color: var(--underline);
    text-underline-offset: 2px;
  }
  .contact__title { font-size: 11px; line-height: 12px; margin-top: 1px; }
  .contact__text { font-size: 11px; line-height: 14px; }

  /* Reach side */
  .brand-name--reach {
    left: 0;
    right: 0;
    top: 99px;
    font-size: 27px;
    letter-spacing: 2px;
    text-align: center;
  }

  .address {
    position: absolute;
    left: 0;
    right: 0;
    top: 180px;
    text-align: center;
    font-size: 12.5px;
    color: var(--muted);
  }
</style>
</head>
<body>

  <section class="card card--chief" aria-label="Card back">
    <svg class="card__bands" viewBox="0 0 430 239" aria-hidden="true">
      <polygon points="0,33 262,33 254,37 0,37"/>
      <polygon points="283,204 430,204 430,208 276,208"/>
    </svg>

    <p class="brand-name brand-name--chief">BRIGHTLANE CHIEF</p>

    <p class="quote">
      "The fastest way to success is to take action"<br>
      <span class="quote__author">– Dorian Welker, Brightlane Chief</span>
    </p>

    <div class="contact">
      <div class="contact__row" style="top:0">
        <svg class="contact__icon" viewBox="0 0 10 10" aria-hidden="true">
          <circle cx="5" cy="3" r="2.3"/><path d="M1 10 Q1 6 5 6 Q9 6 9 10 Z"/>
        </svg>
        <div>
          <div class="contact__name">Dorian Welker</div>
          <div class="contact__title">CEO</div>
        </div>
      </div>
      <div class="contact__row" style="top:35px">
        <svg class="contact__icon" viewBox="0 0 10 10" aria-hidden="true">
          <path d="M2 0.5 L3.6 0.5 L4.3 3 L3.1 4 Q4.2 6.2 6 7 L7 5.8 L9.5 6.5 L9.5 8.2 Q9.5 9.5 8 9.5 Q1 8.5 0.5 2 Q0.5 0.5 2 0.5 Z"/>
        </svg>
        <span class="contact__text">555-204-3378</span>
      </div>
      <div class="contact__row" style="top:59px">
        <svg class="contact__icon" viewBox="0 0 10 10" aria-hidden="true">
          <path d="M0.5 4 L5 1 L9.5 4 L9.5 9 L0.5 9 Z"/><path d="M0.5 4 L5 7 L9.5 4" fill="none" stroke="#fff" stroke-width="0.9"/>
        </svg>
        <span class="contact__text">Dorian@BrightlaneChief.com</span>
      </div>
    </div>
  </section>

  <section class="card card--reach" aria-label="Card front">
    <svg class="card__bands" viewBox="0 0 430 239" aria-hidden="true">
      <polygon points="166,31 430,31 430,35 174,35"/>
      <polygon points="0,204 262,204 270,208 0,208"/>
    </svg>

    <p class="brand-name brand-name--reach">BRIGHTLANE REACH</p>

    <p class="address">247 E. Pelham Row 5th Floor San Diego CA 92384</p>
  </section>

</body>
</html>
```